Popup Banners - BrightCounsel - Legal Technology

- We need two banners (same style) designed with two different images and different text.

- The details of the printing requirements are attached, along with suggested images.

- The banners should share the same theme as our website www.brightcounsel.com.au

- The first banner would include our logo (attached), use the 'roads join' image (attached) in some way and text: New Opportunities - Where legal services and technology meet.

- The second banner would include our logo (attached), use the 'jigsaw' image (attached) in some way and use text: Legal Technology Strategy, Advice and Capability.

- Details on what are required from the Printer is attached also.

Target Market(s)

Legal Professionals

Industry/Entity Type

Information Technology

Font styles to use
Sans Serif

Requirements
Must have
• Our logo (attached), suggested text and the image mentioned for each.
Nice to have
• Professional and modern look
Should not have
• Cheap looking

```html
<!DOCTYPE html>
<html lang="en">
<head>
<meta charset="utf-8">
<title>BrightCounsel Popup Banners</title>
<link rel="stylesheet" href="https://fonts.googleapis.com/css2?family=Barlow+Semi+Condensed:wght@400&family=Barlow:wght@400&display=swap">
<style>
  :root {
    --page-bg: #ffffff;
    --brand-blue: #3872ae;
    --brand-navy: #1b2a3c;
    --banner-white: #ffffff;
    --headline: #ffffff;
    --wordmark: #5a5350;
    --accent-square: #4a90d0;
    --shadow: rgba(0, 0, 0, 0.18);
  }
  * { box-sizing: border-box; margin: 0; padding: 0; }
  html, body {
    width: 1200px;
    height: 1200px;
    overflow: hidden;
    background: var(--page-bg);
  }
  .canvas {
    position: relative;
    width: 1200px;
    height: 1200px;
  }
  .banner {
    position: absolute;
    width: 402px;
    height: 993px;
    background: var(--banner-white);
    box-shadow: 0 6px 14px var(--shadow);
    overflow: hidden;
  }
  .banner--roads { left: 138px; top: 103px; --band: var(--brand-blue); }
  .banner--jigsaw { left: 695px; top: 102px; --band: var(--brand-navy); }

  .banner__head {
    position: absolute;
    left: 0; top: 0;
    width: 100%;
    background: var(--band);
  }
  .banner--roads .banner__head { height: 150px; }
  .banner--jigsaw .banner__head { height: 124px; }

  .banner__headline {
    position: absolute;
    left: 21px;
    top: 38px;
    font-family: "Barlow Semi Condensed", "Barlow", sans-serif;
    font-weight: 400;
    font-size: 23px;
    line-height: 38px;
    letter-spacing: 0.6px;
    text-transform: uppercase;
    color: var(--headline);
  }

  .banner__visual {
    position: absolute;
    left: 0;
    width: 100%;
  }
  .banner--roads .banner__visual {
    top: 150px;
    height: 235px;
    background: linear-gradient(180deg, #3f7fc2 0%, #7fb0dc 12%, #6f9a3c 18%, #4f8a2a 55%, #3f7a22 100%);
  }
  .banner--jigsaw .banner__visual {
    top: 124px;
    height: 261px;
    background:
      radial-gradient(circle at 62% 40%, #e8f4ff 0%, #7fb4e0 12%, #2f5f8f 35%, #13304f 70%, #0d2036 100%);
  }

  .banner__brand {
    position: absolute;
    right: 23px;
    top: 404px;
    display: flex;
    align-items: center;
    gap: 12px;
  }
  .brand__square {
    width: 16px;
    height: 16px;
    background: var(--accent-square);
  }
  .brand__name {
    font-family: "Barlow", sans-serif;
    font-weight: 400;
    font-size: 23px;
    letter-spacing: 3.2px;
    color: var(--wordmark);
  }

  .banner__foot {
    position: absolute;
    left: 0; bottom: 0;
    width: 100%;
    height: 152px;
    background: var(--band);
  }
</style>
</head>
<body>
<main class="canvas">

  <section class="banner banner--roads">
    <div class="banner__head">
      <h1 class="banner__headline">New opportunities -<br>where legal services<br>and technology come together</h1>
    </div>
    <div class="banner__visual" role="img" aria-label="Photo of two dirt roads joining across a green grassy hill under a blue sky"></div>
    <div class="banner__brand">
      <span class="brand__square"></span>
      <span class="brand__name">BrightCounsel</span>
    </div>
    <div class="banner__foot"></div>
  </section>

  <section class="banner banner--jigsaw">
    <div class="banner__head">
      <h1 class="banner__headline">Legal technology strategy,<br>advice and capability</h1>
    </div>
    <div class="banner__visual" role="img" aria-label="Photo of a hand placing a glowing jigsaw piece into a dark blue puzzle"></div>
    <div class="banner__brand">
      <span class="brand__square"></span>
      <span class="brand__name">BrightCounsel</span>
    </div>
    <div class="banner__foot"></div>
  </section>

</main>
</body>
</html>
```